TKA Electricial Contracting Services

Hi guys, after a design for my small electrical company, have logo design files to be incorporated into the layout, the basic concept is electrical contracting services for residential, commercial, industrial & data services, image is clean clear and strong,

Card format is to have a nice clean logo on front,with maybe the Residential – commercial – industrial - data, followed with licensed & insured, followed by contact details on backside of the card.

Target Market(s)

Residential, commercial, industrial sectors.

Industry/Entity Type

Electrical

Contact Information for Business Card

TKA logo,
Residential – commercial – industrial - data
REC: 61372
Email: tka@poralink.net.au
Phone: 0458 203 719

Requirements
Must have
• Clean & strong design.
Nice to have
• If possible, I would like the logo colours inverted so the text is orange and the background is black on the front of the card, then the backside of the card be the reverse colour
Should not have
• No Sparks, lightning bolts,

```html
<!DOCTYPE html>
<html lang="en">
<head>
<meta charset="UTF-8">
<title>TKA Electrical Contracting Services – Business Card</title>
<link rel="stylesheet" href="https://fonts.googleapis.com/css2?family=Ubuntu:wght@300;400;700&display=swap">
<style>
  :root {
    --stage: #ececec;
    --ink: #111111;
    --card-dark: #161616;
    --card-light: #f4f4f2;
    --paper-text: #e9e9e9;
    --rule-light: #bdbdbd;
    --rule-dark: #1a1a1a;
    --muted: #6d6d6d;
    --band-tone: #d6d6d4;
  }
  * { box-sizing: border-box; margin: 0; padding: 0; }
  html, body {
    width: 1200px; height: 720px; overflow: hidden;
    background: var(--stage);
    font-family: "Ubuntu", Arial, sans-serif;
  }
  .stage {
    position: relative; width: 1200px; height: 720px;
    display: flex; align-items: center; justify-content: center; gap: 60px;
  }
  .card {
    position: relative; width: 520px; height: 318px;
    box-shadow: 0 2px 6px rgba(0,0,0,.08);
  }

  /* Front */
  .card--front { background: var(--card-dark); color: var(--paper-text); }
  .front__brand {
    position: absolute; left: 0; right: 0; top: 62px; text-align: center;
  }
  .brand-name {
    font-weight: 700; font-size: 108px; line-height: 1; letter-spacing: -2px;
  }
  .front__company {
    margin-top: 6px; font-weight: 400; font-size: 22px; letter-spacing: .5px;
  }
  .front__services {
    position: absolute; left: 60px; right: 60px; bottom: 36px;
    border-top: 1px solid var(--rule-light);
    border-bottom: 1px solid var(--rule-light);
    padding: 9px 0; text-align: center;
    font-size: 13px; letter-spacing: .6px; text-transform: uppercase;
  }

  /* Back */
  .card--back { background: var(--card-light); color: var(--ink); }
  .back__frame {
    position: absolute; inset: 16px; border: 1.5px solid var(--rule-dark);
    display: grid; grid-template-rows: 54px 1fr 48px;
  }
  .back__header {
    position: relative; border-bottom: 1.5px solid var(--rule-dark);
    background: var(--band-tone);
    display: flex; align-items: center; justify-content: center;
  }
  .back__header-inner {
    background: var(--card-light); border: 1px solid var(--rule-light);
    padding: 6px 22px; font-weight: 300; font-size: 15px;
    letter-spacing: 1px; text-transform: uppercase; color: var(--muted);
  }
  .back__brand {
    display: flex; flex-direction: column; align-items: center; justify-content: center;
  }
  .back__brand .brand-name { font-size: 96px; }
  .back__services {
    margin-top: 4px; font-size: 12.5px; letter-spacing: .5px; text-transform: uppercase;
  }
  .back__contacts {
    display: grid; grid-template-columns: 1.1fr 1fr 1.4fr;
    border-top: 1.5px solid var(--rule-dark); font-size: 13.5px;
  }
  .contact {
    display: flex; align-items: center; justify-content: center;
    border-right: 1.5px solid var(--rule-dark);
  }
  .contact:last-child { border-right: 0; }
  .contact--licence { background: var(--rule-dark); color: var(--paper-text); letter-spacing: .5px; }
</style>
</head>
<body>
<main class="stage">
  <section class="card card--front" aria-label="Card front">
    <div class="front__brand">
      <div class="brand-name">TKA</div>
      <div class="front__company">Tyler Kane Electrical</div>
    </div>
    <div class="front__services">Residential – Commercial – Industrial – Data</div>
  </section>

  <section class="card card--back" aria-label="Card back">
    <div class="back__frame">
      <header class="back__header" role="img" aria-label="Diagonal hatched band behind the company name">
        <span class="back__header-inner">Tyler Kane Electrical</span>
      </header>
      <div class="back__brand">
        <div class="brand-name">TKA</div>
        <div class="back__services">Residential – Commercial – Industrial – Data</div>
      </div>
      <footer class="back__contacts">
        <div class="contact contact--licence">REC: 61372</div>
        <div class="contact contact--phone">0458 203 719</div>
        <div class="contact contact--email">tka@poralink.net.au</div>
      </footer>
    </div>
  </section>
</main>
</body>
</html>
```